Quillforge new logo business card

We need a business card designed to promote the new direction of our company. Originally (for the past 12 years) we were a design-based marketing consultancy specialising in B2B. But now we are offering marketing consultancy to companies in the ecommerce business. We have expertise in this and operate three online stores ourselves and can provide warehousing and distribution services.
The new logo and business card should reflect this market - e.g. modern, technical, commercial but also creative!
Our current logo is too 'designery' and doesn't reflect the seriousness and professionalism of our current business. It also is very long and thin so doesnot work well in rectangular panels.
The name 'Quillforge' comprises two parts - Quill and Forge and these parts of the word can have a different type font or colour. The 'Quill' element is the creative element while the 'Forge' part is the technical, businesslike part. We can also look at 'The Quillforge Company' rather than just 'quillforge.' We can also include the slogan 'Source, Sell, Succeed.' under the logo.
The address details for the card are 7 Larchmere Rise, Woking, Surrey RH14 3TN. We will also need an email address and phone number (details will be supplied later)
On the back of the card will be a list of services offered.
Quillforge can help your business succeed through:
Product Sourcing
Marketing
Distribution
Storage
Ecommerce

Target Market(s)

Owners of small and medium-sized retail businesses - particularly mail order and ecommerce based businesses.

Industry/Entity Type

Marketing

Requirements
Must have
• The company name should be prominent. This can either be 'Quillforge' or 'The Quillforge Company'.
• Then the words 'Quillforge Ltd, Unit F, Ashcombe Trade Park, Millrace Way, Ashcombe, Woking, Surrey RH17 9LW
• 0844 312 5809 www.thequillforge-example.co.uk
• Must also include cardholder's name and title.
• Gideon Halbrook
• Director
• On the reverse it should say.
• Quillforge - Developing profitable brands in a multi-channel environment

```html
<!DOCTYPE html>
<html lang="en">
<head>
<meta charset="utf-8">
<title>Quillforge business card</title>
<link rel="stylesheet" href="https://fonts.googleapis.com/css2?family=Tinos:wght@400;700&display=swap">
<style>
  :root {
    --navy: #233a78;
    --red: #e8282f;
    --paper: #f7f7f7;
    --stage: #2a2a2a;
    --serif: "Tinos", "Times New Roman", serif;
  }
  * { box-sizing: border-box; margin: 0; padding: 0; }
  html, body { width: 1200px; height: 899px; overflow: hidden; background: var(--stage); }
  .canvas { position: relative; width: 1200px; height: 899px; }

  .card { position: absolute; width: 560px; height: 320px; background: var(--paper); overflow: hidden; }
  .card svg.shapes { position: absolute; inset: 0; width: 100%; height: 100%; }
  .card-back { left: 480px; top: 80px; }
  .card-front { left: 160px; top: 490px; }

  .wordmark { font-family: var(--serif); color: var(--navy); font-size: 36px; letter-spacing: 1px; line-height: 1; }

  /* back */
  .services { position: absolute; left: 26px; top: 26px; color: #fff; font-family: var(--serif); }
  .services-lead { font-weight: 700; font-size: 18px; }
  .services-list { list-style: none; margin: 8px 0 0 18px; font-size: 17px; line-height: 1.05; }
  .card-back .wordmark { position: absolute; right: 26px; bottom: 56px; }

  /* front */
  .card-front .wordmark { position: absolute; left: 22px; top: 40px; }
  .holder { position: absolute; left: 22px; top: 120px; color: #fff; font-family: var(--serif); text-align: center; }
  .holder-name { font-size: 22px; font-weight: 700; }
  .holder-title { font-size: 15px; font-weight: 700; }
  .contact { position: absolute; left: 205px; top: 190px; font-family: var(--serif); color: var(--navy); font-size: 15px; list-style: none; }
  .contact li { display: flex; align-items: center; gap: 10px; height: 24px; }
  .contact svg { width: 15px; height: 15px; fill: var(--navy); flex: none; }
  .contact .spacer { margin-left: 30px; }
</style>
</head>
<body>
<main class="canvas">

  <section class="card card-back" aria-label="Card reverse">
    <svg class="shapes" viewBox="0 0 560 320" preserveAspectRatio="none" aria-hidden="true">
      <path d="M410,0 H560 V4 C430,150 230,280 0,320 H0 C200,280 340,160 410,0 Z" fill="var(--red)"/>
      <path d="M0,0 H410 C340,160 200,280 0,314 Z" fill="var(--navy)"/>
    </svg>
    <div class="services">
      <p class="services-lead">Developing profitable brands through</p>
      <ul class="services-list">
        <li>Product Sourcing</li>
        <li>Marketing</li>
        <li>Distribution</li>
        <li>Storage</li>
        <li>Ecommerce</li>
      </ul>
    </div>
    <p class="wordmark">QUILLFORGE</p>
  </section>

  <section class="card card-front" aria-label="Card front">
    <svg class="shapes" viewBox="0 0 560 320" preserveAspectRatio="none" aria-hidden="true">
      <path d="M0,0 H560 V22 L0,10 Z" fill="var(--navy)"/>
      <path d="M0,112 H190 L268,140 C170,170 70,230 0,272 Z" fill="var(--navy)"/>
      <path d="M0,282 C150,190 330,130 540,102 C360,140 220,210 120,320 H0 Z" fill="var(--red)"/>
    </svg>
    <p class="wordmark">QUILLFORGE</p>
    <div class="holder">
      <p class="holder-name">Gideon Halbrook</p>
      <p class="holder-title">Director</p>
    </div>
    <ul class="contact">
      <li><svg viewBox="0 0 16 16"><path d="M8,1 L1,8 H3 V15 H7 V10 H9 V15 H13 V8 H15 Z"/></svg>7 Larchmere Rise, Woking, Surrey RH14 3TN</li>
      <li><svg viewBox="0 0 16 16"><path d="M1,6 C1,3 15,3 15,6 V8 H11 V6 H5 V8 H1 Z M4,9 H12 L14,14 H2 Z"/></svg>01632 960418
        <svg class="spacer" viewBox="0 0 16 16"><path d="M1,6 C1,3 15,3 15,6 V8 H11 V6 H5 V8 H1 Z M4,9 H12 L14,14 H2 Z"/></svg>07700 900372</li>
      <li><svg viewBox="0 0 16 16"><path d="M1,3 H15 V13 H1 Z M2,4 L8,9 L14,4" fill="none" stroke="var(--navy)" stroke-width="1.5"/></svg>gideon@thequillforge-example.co.uk</li>
      <li><svg viewBox="0 0 16 16"><g fill="none" stroke="var(--navy)" stroke-width="1.2"><circle cx="8" cy="8" r="6.5"/><ellipse cx="8" cy="8" rx="3" ry="6.5"/><path d="M1.5,8 H14.5 M2.5,5 H13.5 M2.5,11 H13.5"/></g></svg>www.thequillforge-example.co.uk</li>
    </ul>
  </section>

</main>
</body>
</html>
```